Oil Field Service company needs professional business cards

Looking to clean up our current company business cards and look a little more professional. Harlow Tubular Services is a US based company that services the oil field. We deal with engineers, managers and oil rigs....................................................................................................................................................................................................................................................................................................................................................................................................

Target Market(s)

Oil and Gas professionals

Industry/Entity Type

Oil And Gas

Contact Information for Business Card

See attached photo as example

Font styles to use
Sans Serif

Colors
ec1f27

Requirements
Must have
• Company Logo, Name, Title, Cell, Office, Fax, Email.
• See attached photo
Nice to have
• External CRT, Internal CRT, Casing Crews, Torque Turn, Laydown Machine
Should not have
• Do not introduce any new pictures and keep it professional looking

```html
<!DOCTYPE html>
<html lang="en">
<head>
<meta charset="utf-8">
<title>Harlow Tubular Services – Business Card</title>
<link rel="stylesheet" href="https://fonts.googleapis.com/css2?family=Arimo:wght@400;700&display=swap">
<style>
  :root {
    --brand-red: #e4222b;
    --slate: #48555f;
    --ink: #000000;
    --paper: #ffffff;
    --frame: #111111;
  }
  html, body {
    margin: 0;
    padding: 0;
    width: 1200px;
    height: 765px;
    overflow: hidden;
    background: var(--paper);
    font-family: "Arimo", Arial, sans-serif;
  }
  .card {
    position: absolute;
    left: 34px;
    top: 38px;
    width: 1132px;
    height: 690px;
    border: 2px solid var(--frame);
    background: var(--paper);
    overflow: hidden;
  }
  .brand {
    position: absolute;
    left: 0;
    right: 0;
    top: 62px;
    text-align: center;
    color: var(--slate);
    font-weight: 700;
    line-height: 1;
  }
  .brand-main {
    display: block;
    font-size: 84px;
    letter-spacing: 2px;
  }
  .brand-sub {
    display: block;
    margin-top: 26px;
    font-size: 25px;
    letter-spacing: 4px;
  }
  .contact {
    position: absolute;
    left: 0;
    right: 0;
    top: 242px;
    text-align: center;
    color: var(--ink);
  }
  .person-name {
    margin: 0;
    font-size: 39px;
    font-weight: 700;
    line-height: 46px;
  }
  .person-title {
    margin: 0;
    font-size: 36px;
    font-weight: 700;
    line-height: 46px;
  }
  .person-cell {
    margin: 0;
    font-size: 33px;
    font-weight: 700;
    line-height: 40px;
  }
  .details {
    margin: 18px 0 0;
    padding: 0;
    list-style: none;
    font-size: 33px;
    font-weight: 400;
    line-height: 40px;
  }
  .footer-band {
    position: absolute;
    left: 0;
    bottom: 0;
    width: 1132px;
    height: 150px;
  }
  .services {
    position: absolute;
    left: 0;
    right: 0;
    bottom: 24px;
    margin: 0;
    text-align: center;
    color: var(--paper);
    font-size: 31px;
    font-weight: 700;
    line-height: 39px;
  }
</style>
</head>
<body>
  <div class="card">
    <div class="brand">
      <span class="brand-main">HARLOW</span>
      <span class="brand-sub">TUBULAR SERVICES</span>
    </div>

    <div class="contact">
      <p class="person-name">CASEY BRANDVOLD</p>
      <p class="person-title">AREA MANAGER</p>
      <p class="person-cell">Cell:(555) 214 3870</p>
      <ul class="details">
        <li>Office :(555) 362 9104</li>
        <li>Fax :(555) 214 6652</li>
        <li>E mail : name@harlowtubular.com</li>
      </ul>
    </div>

    <svg class="footer-band" viewBox="0 0 1132 150" preserveAspectRatio="none" aria-hidden="true">
      <path d="M0 96 Q566 -92 1132 96 L1132 150 L0 150 Z" fill="var(--brand-red)"/>
    </svg>
    <p class="services">EXTERNAL CRT, INTERNAL CRT,<br>CASING CREWS, TORQUE TURN, LAYDOWN MACHINE</p>
  </div>
</body>
</html>
```